Business Card for By Marcus Hale

Looking to have a business card designed for my lifestyle and fitness company. My company offers personal training, online programming and nutrition advice based out of London, United Kingdom.

I'd like to see modern, sleek designs, focusing on black, matte black or matte grey. Design doesn't need to be overly descriptive as this will also be used as a personal business card. I've included my logo.

Please note that my company is no longer called "Fitness by Marcus Hale" but instead "By Marcus Hale", this is because of my other ventures. Therefore please don't use the "fitness by marcus hale" text.

information about my company can be found at www.bymarcushale.com

Company is also based out of London (United Kingdom) & Sydney (Australia) this could be reflected on the card.

Industry/Entity Type

Business

Contact Information for Business Card

Marcus Hale
+44 7382 615204
marcus@bymarcushale.com
www.bymarcushale.com

Font styles to use
Sans Serif

Requirements
Must have
• All contact details and inclusion of my logo.

```html
<!DOCTYPE html>
<html lang="en">
<head>
<meta charset="UTF-8">
<title>By Marcus Hale — Business Card</title>
<link href="https://fonts.googleapis.com/css2?family=Montserrat:wght@400;500;600&family=Open+Sans:wght@400&display=swap" rel="stylesheet">
<style>
  :root {
    --backdrop: #c9d3db;
    --card-dark: #1c1f22;
    --card-mid: #2c3034;
    --ink-white: #f2f3f4;
    --ink-soft: #c4c8cc;
    --rule: #8d9296;
  }
  * { margin: 0; padding: 0; box-sizing: border-box; }
  html, body {
    width: 1200px;
    height: 1200px;
    overflow: hidden;
    background: var(--backdrop);
  }
  .canvas {
    width: 1200px;
    height: 1200px;
    display: flex;
    flex-direction: column;
    align-items: center;
    justify-content: center;
    gap: 70px;
  }
  .card {
    position: relative;
    width: 860px;
    height: 491px;
    background: linear-gradient(160deg, var(--card-mid) 0%, var(--card-dark) 70%);
    box-shadow: 0 18px 40px rgba(20, 30, 40, 0.28);
    color: var(--ink-white);
  }
  .wordmark {
    display: flex;
    align-items: center;
    gap: 14px;
    font-family: "Montserrat", sans-serif;
    font-weight: 600;
    text-transform: uppercase;
    letter-spacing: 0.08em;
    color: var(--ink-white);
    white-space: nowrap;
  }
  .wordmark-dot {
    width: 14px;
    height: 14px;
    border-radius: 50%;
    background: var(--ink-white);
    flex: none;
  }
  .card-front {
    display: flex;
    align-items: center;
    justify-content: center;
  }
  .card-front .wordmark { font-size: 34px; }

  .card-back .brand {
    position: absolute;
    left: 0;
    top: 0;
    width: 390px;
    height: 100%;
    display: flex;
    align-items: center;
    justify-content: center;
  }
  .card-back .wordmark { font-size: 28px; }
  .divider {
    position: absolute;
    left: 398px;
    top: 118px;
    width: 1px;
    height: 250px;
    background: linear-gradient(180deg, transparent, var(--rule) 20%, var(--rule) 80%, transparent);
  }
  .details {
    position: absolute;
    left: 440px;
    top: 126px;
    width: 360px;
  }
  .holder-name {
    font-family: "Montserrat", sans-serif;
    font-weight: 500;
    font-size: 30px;
    letter-spacing: 0.02em;
    text-transform: uppercase;
    padding-bottom: 12px;
    border-bottom: 1px solid var(--rule);
    display: inline-block;
    padding-right: 26px;
  }
  .contact-list {
    list-style: none;
    margin-top: 42px;
    display: flex;
    flex-direction: column;
    gap: 14px;
  }
  .contact-item {
    display: flex;
    align-items: center;
    gap: 22px;
    font-family: "Open Sans", sans-serif;
    font-size: 18px;
    color: var(--ink-soft);
  }
  .contact-icon {
    width: 18px;
    height: 18px;
    flex: none;
    fill: var(--ink-white);
  }
</style>
</head>
<body>
<main class="canvas">
  <section class="card card-front" aria-label="Card front">
    <div class="wordmark"><span class="wordmark-dot"></span>By Marcus Hale</div>
  </section>

  <section class="card card-back" aria-label="Card back">
    <div class="brand">
      <div class="wordmark"><span class="wordmark-dot"></span>By Marcus Hale</div>
    </div>
    <div class="divider"></div>
    <div class="details">
      <h1 class="holder-name">Marcus Hale</h1>
      <ul class="contact-list">
        <li class="contact-item">
          <svg class="contact-icon" viewBox="0 0 24 24" aria-hidden="true"><path d="M6.6 10.8a15.1 15.1 0 0 0 6.6 6.6l2.2-2.2c.3-.3.7-.4 1-.2 1.1.4 2.3.6 3.6.6.6 0 1 .4 1 1V20c0 .6-.4 1-1 1C10.6 21 3 13.4 3 4c0-.6.4-1 1-1h3.5c.6 0 1 .4 1 1 0 1.3.2 2.5.6 3.6.1.3 0 .7-.2 1z"/></svg>
          <span>+44 7382 615204</span>
        </li>
        <li class="contact-item">
          <svg class="contact-icon" viewBox="0 0 24 24" aria-hidden="true"><path d="M2 5h20v14H2z M4 7v.5l8 5.5 8-5.5V7z" fill-rule="evenodd"/></svg>
          <span>marcus@bymarcushale.com</span>
        </li>
        <li class="contact-item">
          <svg class="contact-icon" viewBox="0 0 24 24" aria-hidden="true"><path d="M12 2a10 10 0 1 0 0 20 10 10 0 0 0 0-20zm-1 17.9A8 8 0 0 1 4.1 11H7c.1 3.3 1.5 6.5 4 8.9zM7 9H4.1A8 8 0 0 1 11 4.1C8.5 6.5 7.1 5.7 7 9zm2 2h6c-.1 2.8-1.2 5.4-3 7.4-1.8-2-2.9-4.6-3-7.4zm0-2c.1-2.8 1.2-5.4 3-7.4 1.8 2 2.9 4.6 3 7.4zm4 10.9c2.5-2.4 3.9-5.6 4-8.9h2.9a8 8 0 0 1-6.9 8.9zM17 9c-.1-3.3-1.5-6.5-4-8.9A8 8 0 0 1 19.9 9z"/></svg>
          <span>www.bymarcushale.com</span>
        </li>
      </ul>
    </div>
  </section>
</main>
</body>
</html>
```